Offshore Energy Projects Management Consultancy needs a business card design

Logo available. We provide teams to deliver engineering consultancy, project management and delivery teams mainly in the offshore renewables sector. The company is all about bringing the right people to a project to deliver the scope.

The business card will be used for all staff.

The business card should be quite simple, vibrant and uncluttered but convey experience, enthusiasm and integration.

Target Market(s)

Energy Project Developers and Tier 1 construction companies

Contact Information for Business Card

Logo should be on the back of the card. I'm happy for the designer to play with the colour of the logo and background colour.

Front of the card should convey all the must have information in a clear and professional manner but without being overly traditional.

Colors

Designer to choose colors to be used in the design.

Requirements
Must have
• Land Line Tel Number, Mobile Tel Number, Email, business address, web address.

```html
<!DOCTYPE html>
<html lang="en">
<head>
<meta charset="utf-8">
<title>Business Card – Front</title>
<link rel="stylesheet" href="https://fonts.googleapis.com/css2?family=Ubuntu:wght@300;400&display=swap">
<style>
  :root {
    --backdrop: #ececec;
    --card: #ffffff;
    --navy: #3b5fa4;
    --teal: #1b8fc1;
    --divider-green: #8cc265;
    --separator: #1aa3c9;
  }
  html, body {
    margin: 0;
    padding: 0;
    width: 1200px;
    height: 784px;
    overflow: hidden;
    background: var(--backdrop);
  }
  .card-front {
    position: absolute;
    left: 126px;
    top: 85px;
    width: 948px;
    height: 612px;
    background: var(--card);
    font-family: "Ubuntu", sans-serif;
    text-align: center;
  }
  .card-front > * {
    position: absolute;
    left: 0;
    width: 100%;
    margin: 0;
  }
  .person-name {
    top: 101px;
    font-size: 62px;
    font-weight: 400;
    line-height: 1;
    color: var(--navy);
    letter-spacing: 0.2px;
  }
  .job-title {
    top: 174px;
    font-size: 42px;
    font-weight: 300;
    line-height: 1;
    color: var(--teal);
  }
  .divider {
    top: 272px;
    left: 399px;
    width: 131px;
    height: 2px;
    background: var(--divider-green);
  }
  .address {
    top: 316px;
    font-style: normal;
    font-size: 29px;
    font-weight: 400;
    line-height: 39px;
    color: var(--teal);
  }
  .contact-line {
    top: 463px;
    font-size: 29px;
    font-weight: 400;
    line-height: 39px;
    color: var(--navy);
  }
  .contact-line .separator {
    color: var(--separator);
    margin: 0 16px 0 20px;
  }
</style>
</head>
<body>
  <section class="card-front">
    <h1 class="person-name">Daniel Hughes</h1>
    <p class="job-title">Project Manager</p>
    <div class="divider"></div>
    <address class="address">
      The Harbourline Building<br>
      312 Quayside Street<br>
      Northport, NP4 2QL
    </address>
    <p class="contact-line">
      <span class="email">daniel@tideway.ltd</span><span class="separator">|</span><span class="phone">+44 1632 960 418</span>
    </p>
  </section>
</body>
</html>
```